Book cover needed for a major new book on emotional resilience

The book will be titled: 'Storm to Stillness: from rigid habits to pioneers of renewal - The handbook for building steady teams and institutions'
My websites are http://www.brightmarrow.com and http://www.hollenquay.org and I am http://en.pedialoom.org/wiki/Tomas_Brenhurst_(uncertainty_scholar) ad expert in developing emotional resilience. My previous book was The Quiet Compass.
The premise of the book is to introduce brand new material which is the first ever methodology and strategy on how to develop emotional resilience across entire populations like organisations and companies or moving people from fear about change to finding flow through resilience.
The final design should communicate the fact that this is a strategy and methodology. That it is about developing people and entire organisations to be more resilient and who are able to deal with change better.
Target Market(s)
Consultants, Organisational development consultants, Human Resource professionals.

```html
<!DOCTYPE html>
<html lang="en">
<head>
<meta charset="utf-8">
<title>Storm to Stillness – Book Cover</title>
<link href="https://fonts.googleapis.com/css2?family=Source+Sans+3:wght@300;400;700&display=swap" rel="stylesheet">
<style>
  :root {
    --page-bg: #ffffff;
    --cover-bg: #ffffff;
    --accent: #ee8a3a;
    --accent-soft: #f6c59c;
    --ink: #555a5e;
    --ink-light: #6b6f72;
    --grid-grey: #e7e8e9;
  }
  * { margin: 0; padding: 0; box-sizing: border-box; }
  html, body {
    width: 1200px;
    height: 900px;
    overflow: hidden;
    background: var(--page-bg);
  }
  .stage {
    position: relative;
    width: 1200px;
    height: 900px;
  }
  .cover {
    position: absolute;
    left: 333px;
    top: 32px;
    width: 545px;
    height: 833px;
    background: var(--cover-bg);
    overflow: hidden;
    font-family: "Source Sans 3", Arial, sans-serif;
    border: 1px solid #f0f0f0;
  }
  .cover-art {
    position: absolute;
    left: 0;
    top: 0;
    width: 545px;
    height: 833px;
  }
  .title {
    position: absolute;
    left: 58px;
    top: 106px;
    font-weight: 300;
    font-size: 45px;
    line-height: 1;
    letter-spacing: -0.5px;
    color: var(--accent);
    white-space: nowrap;
  }
  .subtitle {
    position: absolute;
    left: 58px;
    top: 156px;
    font-weight: 300;
    font-size: 16px;
    color: var(--accent);
    white-space: nowrap;
  }
  .tagline {
    position: absolute;
    left: 58px;
    top: 203px;
    font-weight: 700;
    font-size: 13.5px;
    line-height: 18px;
    letter-spacing: 0.3px;
    color: var(--ink);
    text-transform: uppercase;
  }
  .author {
    position: absolute;
    right: 52px;
    top: 782px;
    font-weight: 400;
    font-size: 12.5px;
    letter-spacing: 0.5px;
    color: var(--ink-light);
    text-transform: uppercase;
  }
</style>
</head>
<body>
<div class="stage">
  <div class="cover">
    <svg class="cover-art" viewBox="0 0 545 833" xmlns="http://www.w3.org/2000/svg">
      <defs>
        <linearGradient id="waveTone" x1="0" y1="0" x2="1" y2="0.4">
          <stop offset="0" stop-color="#f4a870" stop-opacity="0.85"/>
          <stop offset="0.5" stop-color="#f8cfae" stop-opacity="0.55"/>
          <stop offset="1" stop-color="#f3a468" stop-opacity="0.75"/>
        </linearGradient>
        <linearGradient id="waveFade" x1="0" y1="0" x2="0" y2="1">
          <stop offset="0" stop-color="#ffffff" stop-opacity="0"/>
          <stop offset="0.45" stop-color="#ffffff" stop-opacity="0"/>
          <stop offset="1" stop-color="#ffffff" stop-opacity="1"/>
        </linearGradient>
        <linearGradient id="gridTone" x1="0" y1="0" x2="0" y2="1">
          <stop offset="0" stop-color="#f2f2f3" stop-opacity="0"/>
          <stop offset="1" stop-color="#e6e7e8" stop-opacity="1"/>
        </linearGradient>
      </defs>
      <g role="img" aria-label="Flowing orange ribbon waves sweeping across the cover">
        <rect x="0" y="235" width="545" height="330" fill="url(#waveTone)"/>
        <rect x="0" y="235" width="545" height="330" fill="url(#waveFade)"/>
      </g>
      <rect role="img" aria-label="Soft grey curved grid fading in from the bottom" x="0" y="520" width="545" height="313" fill="url(#gridTone)"/>
    </svg>

    <h1 class="title">STORM TO STILLNESS</h1>
    <p class="subtitle">from rigid habits to pioneers of renewal -</p>
    <p class="tagline">The handbook for building<br>steady teams &amp; institutions</p>
    <p class="author">Tomas J. Brenhurst</p>
  </div>
</div>
</body>
</html>
```